Brand Identity Redesign for Harbourline Painting - DELIVERABLE - Brand Guide Poster

DELIVERABLE - Brand Guide Poster (see attached Brand Guide Poster 1 and Brand Guide example 2).
- We are seeking graphic designers who can help us reimagine and revamp our brand identity based on our new Harbourline Painting logo. We are looking for a fresh and modern approach that aligns with our values and attracts our target audience.
- The task involves creating a comprehensive brand identity system that includes:
- Logo variations and usage guidelines
- Colour palette selection and guidelines
- Typography selection and guidelines
- Graphic elements, patterns, or textures
- Visual style guidelines for various applications (e.g., website, social media, marketing materials - online and offline)
- Brand collateral design (business cards, letterheads, brochures, quotes, invoices, proposals, vehicle signage, yard signage, worksite signage, etc.)
- The designer should have experience in brand identity design and a strong portfolio showcasing their skills in creating visually appealing and cohesive brand identities.
- The project will require collaboration, as we will provide our new logo and any specific design preferences, and expect the designer to incorporate these elements while offering their creative expertise.
- The deliverables should be provided in digital formats (e.g., vector files, design software files) and accompanied by a brand guidelines document explaining the proper usage of the brand identity elements. See attached example of brand guidelines poster. A one page guide like this would be awesome.

Target Market(s)

1. Wealthy Home Owners with a primary residence and holiday homes on the Central Coast of NSW Overview: Harbourline Painting works extensively with wealthy home owners on the Central Coast of NSW who own beachside properties. These customers typically require extensive maintenance and protection from corrosion due to the harsh coastal environment. 2. Companies who manage multiple properties in New South Wales.

Industry/Entity Type

Painting and decorating

Font styles to use
Serif
Sans Serif

Requirements
Must have
• Overall style should exude sophistication, professionalism, and attention to detail. The design should convey a sense of craftsmanship and longevity, emphasizing the company's focus on protecting surfaces for long-lasting durability. The logo should be sleek, clean, and modern, while still maintaining a classic and timeless feel. It should be versatile and scalable to ensure it can be used across various marketing materials. Brand guidelines poster - see attached example.
Should not have
• Very bright colours that look cheap. I have attached some logos that will be displayed on all our marketing along with a colour scheme that complements them and the logo. I am, however, very open to suggestions.

```html
<!DOCTYPE html>
<html lang="en">
<head>
<meta charset="utf-8">
<title>Harbourline Painting – Brand Guidelines</title>
<link rel="stylesheet" href="https://fonts.googleapis.com/css2?family=Outfit:wght@400;700&display=swap">
<style>
  :root {
    --black: #000000;
    --charcoal: #3F3F3F;
    --grey: #A6A6A6;
    --silver: #D8D8D6;
    --navy: #022859;
    --sky: #04B2D9;
    --white: #FFFFFF;
    --rule: #E6E6E6;
  }
  * { margin: 0; padding: 0; box-sizing: border-box; }
  html, body { width: 849px; height: 1200px; overflow: hidden; background: var(--black); }
  body { font-family: "Outfit", sans-serif; color: var(--white); }
  .poster { position: relative; width: 849px; height: 1200px; background: var(--black); overflow: hidden; }
  .abs { position: absolute; }

  .pattern-band {
    left: 0; top: 0; width: 849px; height: 146px;
    background: linear-gradient(180deg, #1a1a1a 0%, #0d2340 60%, #02121f 100%);
  }
  .title { left: 0; width: 849px; text-align: center; font-size: 36px; line-height: 1; }
  .title--main { top: 181px; font-weight: 700; letter-spacing: -0.2px; }
  .title--sub { top: 227px; font-weight: 400; }

  .rule-h { height: 1px; background: var(--rule); left: 0; width: 849px; }
  .rule-v { width: 1px; background: var(--rule); }

  .section-label { font-size: 17px; font-weight: 400; line-height: 1; letter-spacing: 0.2px; }
  .section-label::before {
    content: ""; position: absolute; left: -24px; top: 3px;
    width: 1.5px; height: 12px; background: var(--sky);
  }

  .logo-panel { top: 358px; width: 425px; height: 149px; display: flex; align-items: center; justify-content: center; }
  .logo-panel--dark { left: 0; background: var(--black); }
  .logo-panel--light { left: 424px; background: var(--white); }
  .wordmark { font-size: 21px; font-weight: 400; letter-spacing: 3px; text-transform: uppercase; }
  .logo-panel--dark .wordmark { color: var(--white); }
  .logo-panel--light .wordmark { color: var(--black); }

  .font-name { left: 51px; top: 612px; font-size: 37px; font-weight: 700; line-height: 43px; }
  .font-underline { left: 51px; top: 707px; width: 99px; height: 2px; background: var(--white); }
  .font-source { left: 51px; top: 765px; font-size: 17px; color: var(--silver); }

  .weight-label { left: 234px; font-size: 16px; color: var(--silver); line-height: 1; }
  .weight-label--bold { top: 597px; font-weight: 700; }
  .weight-label--regular { top: 728px; font-weight: 400; }
  .specimen { left: 233px; font-size: 68px; line-height: 1; letter-spacing: -1px; }
  .specimen--bold { top: 616px; font-weight: 700; }
  .specimen--regular { top: 746px; font-weight: 400; }
  .alphabet { left: 326px; width: 476px; height: 50px; overflow: visible; }
  .alphabet text { fill: var(--white); font-family: "Outfit", sans-serif; font-size: 19px; }
  .alphabet--bold text { font-weight: 700; }
  .alphabet--regular text { font-weight: 400; }

  .swatch {
    width: 101px; height: 101px; display: flex; align-items: center; justify-content: center;
    font-size: 11px; letter-spacing: 1px; border: 1px solid var(--white);
  }
  .swatch--black { background: var(--black); color: var(--white); }
  .swatch--charcoal { background: var(--charcoal); color: var(--white); border-color: var(--grey); }
  .swatch--grey { background: var(--grey); color: var(--silver); border-color: var(--grey); }
  .swatch--silver { background: var(--silver); color: var(--white); border-color: var(--silver); }
  .swatch--navy { background: var(--navy); color: var(--white); border-color: var(--grey); }
  .swatch--sky { background: var(--sky); color: var(--white); border-color: var(--grey); }
  .swatch--white { background: var(--white); color: var(--black); width: 213px; border-color: var(--white); }

  .pattern-sample {
    left: 586px; top: 936px; width: 263px; height: 209px;
    background: linear-gradient(135deg, #2a2a2a 0%, #0d2340 55%, #063d52 100%);
  }
</style>
</head>
<body>
<main class="poster">
  <div class="abs pattern-band" role="img" aria-label="Geometric cube line pattern in white, sky blue and navy"></div>

  <h1 class="abs title title--main">HARBOURLINE PAINTING</h1>
  <p class="abs title title--sub">BRAND GUIDELINESS</p>

  <div class="abs rule-h" style="top:296px"></div>
  <h2 class="abs section-label" style="left:75px; top:319px">MAIN LOGO</h2>
  <div class="abs rule-h" style="top:357px"></div>

  <div class="abs logo-panel logo-panel--dark"><span class="wordmark">Harbourline Painting</span></div>
  <div class="abs logo-panel logo-panel--light"><span class="wordmark">Harbourline Painting</span></div>

  <div class="abs rule-h" style="top:507px"></div>
  <h2 class="abs section-label" style="left:75px; top:531px">TYPOGRAPHY</h2>
  <div class="abs rule-h" style="top:569px"></div>

  <div class="abs rule-v" style="left:212px; top:570px; height:259px"></div>
  <div class="abs rule-h" style="left:212px; width:637px; top:708px"></div>

  <p class="abs font-name">OUTFIT<br>FONT</p>
  <div class="abs font-underline"></div>
  <p class="abs font-source">fonts.harbourline.co</p>

  <p class="abs weight-label weight-label--bold">Outfit Bold</p>
  <p class="abs specimen specimen--bold">Aa</p>
  <svg class="abs alphabet alphabet--bold" style="top:616px" viewBox="0 0 476 50">
    <text x="0" y="21" textLength="474" lengthAdjust="spacing">ABCDEFGHIJKLMNOPQRSTUVWXYZ</text>
    <text x="0" y="49" textLength="470" lengthAdjust="spacing">abcdefghijklmnopqrstuvwxyz</text>
  </svg>

  <p class="abs weight-label weight-label--regular">Outfit Regular</p>
  <p class="abs specimen specimen--regular">Aa</p>
  <svg class="abs alphabet alphabet--regular" style="top:747px" viewBox="0 0 476 50">
    <text x="0" y="21" textLength="470" lengthAdjust="spacing">ABCDEFGHIJKLMNOPQRSTUVWXYZ</text>
    <text x="0" y="49" textLength="466" lengthAdjust="spacing">abcdefghijklmnopqrstuvwxyz</text>
  </svg>

  <div class="abs rule-h" style="top:828px"></div>
  <h2 class="abs section-label" style="left:75px; top:851px">COLOR PALETTE</h2>
  <h2 class="abs section-label" style="left:611px; top:851px">PATTERN</h2>
  <div class="abs rule-v" style="left:536px; top:829px; height:371px"></div>
  <div class="abs rule-h" style="top:890px"></div>

  <div class="abs swatch swatch--black" style="left:51px; top:936px">#000000</div>
  <div class="abs swatch swatch--charcoal" style="left:162px; top:936px">#3F3F3F</div>
  <div class="abs swatch swatch--grey" style="left:273px; top:936px">#A6A6A6</div>
  <div class="abs swatch swatch--silver" style="left:385px; top:936px">#D8D8D6</div>
  <div class="abs swatch swatch--navy" style="left:51px; top:1049px">#022859</div>
  <div class="abs swatch swatch--sky" style="left:162px; top:1049px">#04B2D9</div>
  <div class="abs swatch swatch--white" style="left:273px; top:1049px">#FFFFFF</div>

  <div class="abs pattern-sample" role="img" aria-label="Brand pattern: geometric cube line motif in white with sky blue and navy accents"></div>
</main>
</body>
</html>
```